Via Lumo K

Need business cards designed. Project is an Vesper Hall in Hollywood. It'll include 3 live theatre, a restaurant and event space.

Target Market(s)

Across the board, young and old.

Industry/Entity Type

Entertainment

Contact Information for Business Card

Be creative. This is a creative venture that I'm building.

```html
<!DOCTYPE html>
<html lang="en">
<head>
<meta charset="utf-8">
<title>Vesper Hall – Business Cards</title>
<link rel="stylesheet" href="https://fonts.googleapis.com/css2?family=Questrial&family=Montserrat:wght@700&display=swap">
<style>
  :root {
    --backdrop: #161515;
    --card: #2a2929;
    --accent: #d3203a;
    --text-light: #e2e0e0;
    --text-muted: #cfcdcd;
    --icon-bg: #1c1b1b;
    --divider: #3a3939;
  }
  * { margin: 0; padding: 0; box-sizing: border-box; }
  html, body { width: 1200px; height: 854px; overflow: hidden; }
  body {
    background: var(--backdrop);
    position: relative;
    font-family: "Questrial", sans-serif;
  }
  .card {
    position: absolute;
    left: 326px;
    width: 496px;
    height: 279px;
    background: var(--card);
    box-shadow: 0 6px 18px rgba(0,0,0,.6);
    overflow: hidden;
  }
  .card--front { top: 146px; }
  .card--back { top: 445px; }

  .accent-bar {
    position: absolute;
    left: 240px;
    width: 216px;
    height: 4px;
    background: var(--accent);
  }
  .accent-bar--top { top: 0; }
  .accent-bar--bottom { bottom: 0; left: 238px; }
  .divider {
    position: absolute;
    left: 249px; top: 4px; bottom: 4px;
    width: 1px;
    background: var(--divider);
  }

  .brand {
    position: absolute;
    display: flex;
    align-items: center;
    gap: 8px;
    color: var(--accent);
    font-size: 17px;
    letter-spacing: 1px;
    white-space: nowrap;
  }
  .brand__dot {
    width: 14px; height: 14px;
    border-radius: 50%;
    background: var(--accent);
    flex: none;
  }
  .card--front .brand { left: 58px; top: 127px; }
  .card--back .brand { left: 0; right: 0; top: 88px; justify-content: center; font-size: 20px; }

  .person__name {
    position: absolute;
    left: 240px; top: 36px;
    font-size: 31px;
    letter-spacing: 2.4px;
    color: var(--accent);
    font-weight: 400;
    white-space: nowrap;
  }
  .person__role {
    position: absolute;
    left: 241px; top: 79px;
    font-size: 12.5px;
    letter-spacing: 3px;
    color: var(--text-light);
  }

  .contact { position: absolute; left: 240px; top: 131px; list-style: none; }
  .contact__item {
    display: flex; align-items: center; gap: 14px;
    height: 24px; margin-bottom: 7px;
    font-size: 10px; letter-spacing: 1px;
    color: var(--text-muted);
  }
  .contact__item:last-child { margin-top: 3px; }
  .contact__icon {
    width: 24px; height: 24px; border-radius: 50%;
    background: var(--icon-bg);
    display: flex; align-items: center; justify-content: center;
    flex: none;
  }

  .venue__name {
    position: absolute; left: 0; right: 0; top: 148px;
    text-align: center;
    font-family: "Montserrat", sans-serif;
    font-weight: 700;
    font-size: 29px;
    color: var(--accent);
  }
  .venue__tagline {
    position: absolute; left: 0; right: 0; top: 188px;
    text-align: center;
    font-size: 13.5px;
    letter-spacing: 2px;
    color: var(--text-light);
  }
</style>
</head>
<body>
  <section class="card card--front">
    <span class="accent-bar accent-bar--top"></span>
    <span class="divider"></span>
    <div class="brand"><span class="brand__dot"></span>Via Lumo K</div>

    <h1 class="person__name">Dana Merrow</h1>
    <p class="person__role">CREATIVE DIRECTOR</p>

    <ul class="contact">
      <li class="contact__item">
        <span class="contact__icon">
          <svg width="12" height="12" viewBox="0 0 24 24"><path fill="#d3203a" d="M6.6 10.8a15.1 15.1 0 0 0 6.6 6.6l2.2-2.2a1 1 0 0 1 1-.25 11.4 11.4 0 0 0 3.6.57 1 1 0 0 1 1 1V20a1 1 0 0 1-1 1A17 17 0 0 1 3 4a1 1 0 0 1 1-1h3.5a1 1 0 0 1 1 1c0 1.25.2 2.45.57 3.57a1 1 0 0 1-.25 1z"/></svg>
        </span>
        323.555.0148
      </li>
      <li class="contact__item">
        <span class="contact__icon">
          <svg width="13" height="13" viewBox="0 0 24 24" fill="none" stroke="#d3203a" stroke-width="2"><circle cx="12" cy="12" r="9"/><ellipse cx="12" cy="12" rx="4" ry="9"/><path d="M3 12h18M5 7h14M5 17h14"/></svg>
        </span>
        dmerrow@mail.com
      </li>
      <li class="contact__item">
        <span class="contact__icon">
          <svg width="11" height="13" viewBox="0 0 24 28"><path fill="#d3203a" d="M12 0a10 10 0 0 0-10 10c0 7.5 10 18 10 18s10-10.5 10-18A10 10 0 0 0 12 0zm0 14a4 4 0 1 1 0-8 4 4 0 0 1 0 8z"/></svg>
        </span>
        412 N.Larkin Ave
      </li>
    </ul>
    <span class="accent-bar accent-bar--bottom"></span>
  </section>

  <section class="card card--back">
    <div class="brand"><span class="brand__dot"></span>Via Lumo K</div>
    <h2 class="venue__name">Vesper Hall</h2>
    <p class="venue__tagline">Stage, Kitchen and Gathering hall</p>
  </section>
</body>
</html>
```